Mavro Scrub - Contact/Landing Page

I need a landing page which will essentially be the page that customers will go to from the 'website' link on GMB listing. It will provide a short overview of services which need to be selectable. a little further down can capture some contact details followed by a large Submit Now button etc...

I have some icon/logo's that can be utilised at the bottom of the page as industry type references.

Target Market(s)

End of Lease Cleaning Services

Industry/Entity Type

Cleaning Service

Colors

Designer to choose colors to be used in the design.

Requirements
Must have
• As per description
Should not have
• Colours to match my website mavroscrub.com.au

```html
<!DOCTYPE html>
<html lang="en">
<head>
<meta charset="utf-8">
<title>Mavro Scrub – End of Lease Cleaning</title>
<link rel="stylesheet" href="https://fonts.googleapis.com/css2?family=Source+Sans+3:wght@400;600;700&family=Alegreya:wght@400&display=swap">
<style>
:root{
  --blue:#0a6fcf;
  --blue-light:#3aa2e0;
  --blue-sky:#4fa9e3;
  --ink:#1b1b1b;
  --black:#000;
  --white:#fff;
  --footer:#2b2b2b;
  --muted:#cfcfcf;
}
*{margin:0;padding:0;box-sizing:border-box}
html,body{width:1200px;height:3070px;overflow:hidden;background:var(--white)}
body{position:relative;font-family:"Source Sans 3",Arial,sans-serif;color:var(--ink)}
.abs{position:absolute}

/* header */
.topline{left:0;top:0;width:1200px;height:3px;background:var(--blue)}
.header{left:0;top:3px;width:1200px;height:123px;background:var(--white)}
.logo-blob{left:55px;top:60px;width:310px;height:115px;background:var(--white);border-radius:0 0 155px 155px / 0 0 115px 115px;z-index:3}
.brand{left:148px;top:60px;z-index:4;font-size:34px;font-weight:700;color:var(--blue);width:130px;line-height:36px;text-align:center}
.phone{right:108px;top:28px;display:flex;align-items:center;gap:10px;color:var(--blue-light);font-size:23px;font-weight:600}
.nav{right:108px;top:77px;display:flex;gap:25px;font-size:13.5px;color:#222;letter-spacing:.2px}

/* hero */
.hero{left:0;top:126px;width:1200px;height:580px;background:var(--blue)}
.hero-name{left:0;top:340px;width:1200px;text-align:center;font-size:84px;font-weight:700;color:var(--white);letter-spacing:1px}
.tagline{left:0;top:516px;width:1200px;text-align:center;font-family:"Alegreya",Georgia,serif;font-size:40px;color:#e9f3fc}
.tagline span{display:inline-block;width:2px;height:44px;background:#e9f3fc;vertical-align:middle;margin:0 14px}

/* services */
.section-title{left:0;top:772px;width:1200px;text-align:center;font-size:39px;font-weight:400;color:var(--ink);letter-spacing:.5px}
.section-sub{left:0;top:838px;width:1200px;text-align:center;font-size:18px;line-height:28px;color:#333}
.card{top:942px;width:294px;height:405px}
.card-photo{position:absolute;left:0;top:0;width:294px;height:197px;border-radius:6px 6px 0 0}
.card-panel{position:absolute;left:0;top:208px;width:294px;height:197px;border-radius:0 0 6px 6px;background:var(--black);color:var(--white);text-align:center}
.card.is-selected .card-panel{background:var(--blue)}
.card-arrow{position:absolute;left:125px;top:170px;width:44px;height:40px}
.card-title{margin-top:22px;font-size:20px;font-weight:700;letter-spacing:.3px}
.card-text{margin:10px auto 0;width:240px;font-size:12.5px;line-height:25px}
.card-select{margin-top:7px;font-size:13px;font-weight:700;display:flex;justify-content:center;align-items:center;gap:8px}
.box{width:15px;height:15px;border:1.5px solid var(--white);display:inline-flex;align-items:center;justify-content:center}
.card.is-selected .box{background:var(--white)}

/* appointment */
.appt-bg{left:0;top:1370px;width:1200px;height:842px;background:linear-gradient(180deg,#56ade6 0%,#4aa3e0 55%,#3d98da 100%)}
.appt-title{left:0;top:1660px;width:1200px;text-align:center;font-size:48px;font-weight:700;color:var(--white)}
.appt-sub{left:0;top:1741px;width:1200px;text-align:center;font-size:18px;color:#e8f4fd}
.field{left:215px;width:358px;height:41px;background:var(--white);border:1px solid #d8e6f2;font-size:11px;color:#333;padding:13px 16px}
.submit{left:669px;top:1924px;width:360px;height:82px;border-radius:41px;background:var(--black);color:var(--white);font-size:28px;font-weight:700;display:flex;align-items:center;justify-content:center;letter-spacing:.5px}

/* partners */
.partners-title{left:0;top:2312px;width:1200px;text-align:center;font-size:39px;font-weight:700;color:var(--blue-light)}
.partners-sub{left:0;top:2364px;width:1200px;text-align:center;font-size:17px;color:#222}
.badge{top:2426px;width:227px;height:110px;background:var(--white);box-shadow:0 1px 5px rgba(0,0,0,.25)}
.badge-shape{position:absolute;left:38px;top:25px;width:151px;height:60px;border-radius:6px}
.dots{left:578px;top:2580px;display:flex;gap:8px}
.dot{width:16px;height:16px;border-radius:50%;border:2px solid #2a3c8a}
.dot.is-active{border-color:var(--blue-light);width:17px;height:17px}

/* footer */
.footer{left:0;top:2679px;width:1200px;height:391px;background:var(--footer);color:var(--white)}
.f-title{font-size:23px;font-weight:700}
.f-text{font-size:13.5px;line-height:25px}
.social{display:flex;gap:8px}
.social i{width:33px;height:33px;border-radius:50%;border:1.5px solid #e2a33a;display:block}
.links{list-style:none;font-size:13.5px;line-height:26.5px}
.sub-form{width:308px;height:48px;border:1.5px solid #bdbdbd;display:flex}
.sub-form span{flex:1;font-size:12px;padding:15px 18px}
.sub-form b{width:58px;border-left:1.5px solid #bdbdbd;display:flex;align-items:center;justify-content:center}
.f-rule{left:148px;top:3007px;width:944px;height:1px;background:#4a4a4a}
.copyright{left:0;top:3035px;width:1200px;text-align:center;font-size:13px;color:#e6e6e6}
</style>
</head>
<body>

<div class="abs topline"></div>
<header class="abs header"></header>
<div class="abs logo-blob"></div>
<div class="abs brand">Mavro Scrub</div>
<div class="abs phone">
  <svg width="30" height="30" viewBox="0 0 30 30"><circle cx="15" cy="15" r="13" fill="none" stroke="#3aa2e0" stroke-width="2"/><path d="M10.5 8.5l3 3-1.6 1.8c.8 1.8 2.2 3.2 4 4l1.8-1.6 3 3-2 2c-5 0-10.2-5.2-10.2-10.2z" fill="#3aa2e0"/></svg>
  Call 0400 555 018
</div>
<nav class="abs nav"><span>HOME</span><span>ABOUT</span><span>CLEANING</span><span>CARPETS</span><span>WINDOWS</span><span>PEST CONTROL</span><span>TIPS</span><span>CONTACT</span></nav>

<section class="abs hero"></section>
<svg class="abs" style="left:0;top:560px" width="1200" height="150" viewBox="0 0 1200 150">
  <path d="M0 120 C200 150 380 110 560 70 C760 28 980 40 1140 116 L1200 116 L1200 150 L0 150Z" fill="#fff"/>
  <path d="M535 90 C700 30 920 30 1140 116 C960 58 740 62 535 90Z" fill="#3aa2e0"/>
</svg>
<div class="abs hero-name">Mavro Scrub</div>
<div class="abs tagline">End of Lease Cleaning<span></span>Licensed Pest Control</div>

<h2 class="abs section-title">END OF LEASE SERVICES</h2>
<p class="abs section-sub">Fusce tempor odio quis tellus tempor, et commodo purus lobortis.<br>Morbi nec ante faucibus, fermentum neque quis</p>

<div class="abs card" style="left:148px">
  <div class="card-photo" role="img" aria-label="Gloved hand spraying and wiping a glass surface" style="background:linear-gradient(135deg,#5d6670,#8fb5cf 60%,#3b9fd8)"></div>
  <svg class="card-arrow" viewBox="0 0 44 40"><path d="M22 0L44 22H32V40H12V22H0Z" fill="#000"/></svg>
  <div class="card-panel">
    <div class="card-title">CLEANING</div>
    <p class="card-text">Lorem ipsum dolor sit amet, consectetur adipiscing elit, sed do eiusmod tempor incididunt ut labore</p>
    <div class="card-select">Select <span class="box"></span></div>
  </div>
</div>
<div class="abs card is-selected" style="left:473px">
  <div class="card-photo" role="img" aria-label="Cleaner vacuuming a grey carpet" style="background:linear-gradient(135deg,#a9aeb3,#7d858c 60%,#4a6fb0)"></div>
  <svg class="card-arrow" viewBox="0 0 44 40"><path d="M22 0L44 22H32V40H12V22H0Z" fill="#0a6fcf"/></svg>
  <div class="card-panel">
    <div class="card-title">CARPET CLEANING</div>
    <p class="card-text">Lorem ipsum dolor sit amet, consectetur adipiscing elit, sed do eiusmod tempor incididunt ut labore</p>
    <div class="card-select">Select <span class="box"><svg width="11" height="9" viewBox="0 0 11 9"><path d="M1 4.5l3 3 6-6" fill="none" stroke="#0a6fcf" stroke-width="2"/></svg></span></div>
  </div>
</div>
<div class="abs card" style="left:797px">
  <div class="card-photo" role="img" aria-label="Pest technician spraying inside a kitchen cabinet" style="background:linear-gradient(135deg,#e8e4dc,#c9b79c 60%,#d9a93a)"></div>
  <svg class="card-arrow" viewBox="0 0 44 40"><path d="M22 0L44 22H32V40H12V22H0Z" fill="#000"/></svg>
  <div class="card-panel">
    <div class="card-title">PEST CONTROL</div>
    <p class="card-text">Lorem ipsum dolor sit amet, consectetur adipiscing elit, sed do eiusmod tempor incididunt ut labore</p>
    <div class="card-select">Select <span class="box"></span></div>
  </div>
</div>

<div class="abs appt-bg" role="img" aria-label="Blue-tinted photo of a pest technician spraying by a timber fence"></div>
<svg class="abs" style="left:0;top:1360px" width="1200" height="260" viewBox="0 0 1200 260">
  <path d="M0 0 L0 30 C60 120 220 190 420 200 C640 210 800 120 1000 120 C1100 120 1160 140 1200 160 L1200 0Z" fill="#fff"/>
  <path d="M0 30 C60 120 220 190 420 200 C640 210 800 120 1000 120 C1100 120 1160 140 1200 160 L1200 175 C1150 150 1100 135 1000 136 C800 140 640 228 420 222 C200 216 50 140 0 70Z" fill="#2f93d6"/>
  <path d="M0 55 C70 140 220 196 420 206" fill="none" stroke="#fff" stroke-width="5"/>
</svg>
<h2 class="abs appt-title">Make an Appointment</h2>
<p class="abs appt-sub">Sed ut perspiciatis unde omnis iste natus error sit</p>
<div class="abs field" style="top:1818px">First Name</div>
<div class="abs field" style="top:1881px">Sur Name</div>
<div class="abs field" style="top:1945px">Phone</div>
<div class="abs field" style="top:2008px">Email</div>
<div class="abs field" style="top:2072px">Subject</div>
<div class="abs submit">SUBMIT NOW</div>

<h2 class="abs partners-title">Lorem ipsum dolor sit amet,</h2>
<p class="abs partners-sub">Sed ut perspiciatis unde omnis iste natus error sit</p>
<div class="abs badge" style="left:148px;background:#5fbf2a"><div class="badge-shape" style="background:#7ccf45"></div></div>
<div class="abs badge" style="left:387px"><div class="badge-shape" style="background:#c8ced9"></div></div>
<div class="abs badge" style="left:626px"><div class="badge-shape" style="background:#1a1a1a"></div></div>
<div class="abs badge" style="left:865px"><div class="badge-shape" style="background:#cfd8ea"></div></div>
<div class="abs dots"><span class="dot is-active"></span><span class="dot"></span><span class="dot"></span><span class="dot"></span></div>

<footer class="abs footer">
  <div class="abs" style="left:148px;top:64px;width:320px">
    <div class="f-title">About Mavro Scrub</div>
    <p class="f-text" style="margin-top:14px">Lorem ipsum dolor sit amet, consectetur adipiscing elit, sed do eiusmod tempor incididunt ut labore et dolore magna aliqua. Ut enim ad minim veniam, quis nostrud</p>
    <div class="social" style="margin-top:22px" role="img" aria-label="Social media links"><i></i><i></i><i></i><i></i></div>
  </div>
  <div class="abs" style="left:562px;top:64px">
    <div class="f-title">Quick links</div>
    <ul class="links" style="margin-top:14px"><li>Home</li><li>About Us</li><li>FAQ</li><li>Services</li><li>Contact</li></ul>
  </div>
  <div class="abs" style="left:785px;top:64px">
    <div class="f-title">Mavro Scrub Subscription Box</div>
    <p class="f-text" style="margin-top:12px">The standard Lorem Ipsum passage,</p>
    <div class="sub-form" style="margin-top:22px"><span>Enter your E - mail</span><b><svg width="20" height="14" viewBox="0 0 20 14"><path d="M0 7h17M11 1l6 6-6 6" fill="none" stroke="#fff" stroke-width="2"/></svg></b></div>
  </div>
</footer>
<div class="abs f-rule"></div>
<div class="abs copyright">Mavro Scrub © 2021 All Rights Reserved</div>

</body>
</html>
```